Virtual Assistant/Online Marketing Business Card/Stationary

I need a professional but modern business card/stationary for my company in Dallas called Brivolo. Brivolo is a virtual assistant specializing in online marketing. I would like a unique design that stands out and makes my brand clear. Incorporating the logo is a must and have attached it to this brief.

Target Market(s)

small business owners & entrepreneurs, 35-65

Industry/Entity Type

Business

Contact Information for Business Card

Maren Tolk
marentolk@brivolo.biz
(555) 271-9064
brivolo.biz

Font styles to use
Sans Serif

Colors
f04a50
3176b5
9bcb3c

Requirements
Must have
• Colors that match the logo colors. Logo integration

```html
<!DOCTYPE html>
<html lang="en">
<head>
<meta charset="utf-8">
<title>Brivolo — Business Card</title>
<link href="https://fonts.googleapis.com/css2?family=Lato:wght@400;700&family=Questrial&display=swap" rel="stylesheet">
<style>
  :root {
    --page: #eadfd2;
    --card: #f3f2ef;
    --card-edge: #d9d6d0;
    --green: #9bcb3c;
    --blue: #3176b5;
    --red: #f04a50;
    --ink: #3b3632;
    --brand-box: #2a2522;
    --brand-text: #e4dbd2;
    --white: #ffffff;
  }
  * { margin: 0; padding: 0; box-sizing: border-box; }
  html, body {
    width: 1200px; height: 848px; overflow: hidden;
    background: var(--page);
  }
  .canvas {
    position: relative; width: 1200px; height: 848px;
  }
  .card {
    position: absolute; left: 100px; top: 138px;
    width: 1000px; height: 572px;
    background: var(--card);
    border: 1px solid var(--card-edge);
    border-radius: 30px;
    overflow: hidden;
    box-shadow: 0 18px 40px rgba(90, 60, 30, 0.18);
  }
  .name-band {
    position: absolute; left: 0; top: 205px;
    width: 630px; height: 108px;
    background: var(--green);
  }
  .accent-strip {
    position: absolute; top: 313px; height: 8px;
  }
  .accent-strip--red { left: 250px; width: 210px; background: var(--red); }
  .accent-strip--blue { left: 460px; width: 170px; background: var(--blue); }
  .fold {
    position: absolute; left: 560px; top: 110px;
    width: 80px; height: 260px;
  }
  .name {
    position: absolute; left: 78px; top: 220px;
    font-family: "Questrial", sans-serif;
    font-size: 46px; color: var(--white);
    letter-spacing: 0.5px;
  }
  .job-title {
    position: absolute; left: 80px; top: 277px;
    font-family: "Lato", sans-serif; font-weight: 700;
    font-size: 17px; color: var(--white); letter-spacing: 0.5px;
  }
  .brand-box {
    position: absolute; left: 630px; top: 110px;
    width: 340px; height: 260px;
    background: var(--brand-box);
    display: flex; align-items: center; justify-content: center;
  }
  .brand-name {
    font-family: "Lato", sans-serif; font-weight: 700;
    font-size: 64px; color: var(--brand-text);
  }
  .contact-list {
    position: absolute; left: 80px; top: 372px;
    list-style: none;
    font-family: "Lato", sans-serif; font-size: 28px;
    color: var(--ink);
  }
  .contact-item {
    display: flex; align-items: center; gap: 18px;
    height: 52px;
  }
  .contact-icon { width: 30px; height: 26px; flex: none; }
</style>
</head>
<body>
<main class="canvas">
  <article class="card">
    <div class="name-band"></div>
    <div class="accent-strip accent-strip--red"></div>
    <div class="accent-strip accent-strip--blue"></div>

    <svg class="fold" viewBox="0 0 80 260" aria-hidden="true">
      <polygon points="70,0 70,95 0,95" fill="var(--blue)"/>
      <polygon points="70,211 70,260 30,211" fill="var(--red)"/>
    </svg>

    <div class="brand-box">
      <span class="brand-name">Brivolo</span>
    </div>

    <h1 class="name">Maren Tolk</h1>
    <p class="job-title">JOB TITLE</p>

    <ul class="contact-list">
      <li class="contact-item">
        <svg class="contact-icon" viewBox="0 0 30 26" aria-hidden="true">
          <rect x="2" y="5" width="26" height="17" fill="var(--red)"/>
          <polyline points="2,5 15,15 28,5" fill="none" stroke="var(--card)" stroke-width="2"/>
        </svg>
        marentolk@brivolo.biz
      </li>
      <li class="contact-item">
        <svg class="contact-icon" viewBox="0 0 30 26" aria-hidden="true">
          <path d="M3 9 Q15 1 27 9 L24 12 L20 10 L20 8 Q15 6 10 8 L10 10 L6 12 Z" fill="var(--red)"/>
          <path d="M8 13 L22 13 L26 24 L4 24 Z" fill="var(--red)"/>
          <circle cx="15" cy="18.5" r="3" fill="var(--card)"/>
        </svg>
        (555) 271-9064
      </li>
      <li class="contact-item">
        <svg class="contact-icon" viewBox="0 0 30 26" aria-hidden="true">
          <g fill="none" stroke="var(--red)" stroke-width="2">
            <circle cx="15" cy="13" r="11"/>
            <ellipse cx="15" cy="13" rx="5" ry="11"/>
            <line x1="4" y1="13" x2="26" y2="13"/>
            <line x1="6" y1="7" x2="24" y2="7"/>
            <line x1="6" y1="19" x2="24" y2="19"/>
          </g>
        </svg>
        brivolo.biz
      </li>
    </ul>
  </article>
</main>
</body>
</html>
```